Vemtra Group: Business Card for a high end technology company

We need a cool new design for our business cards using our cloud logo. We are a technology consulting business. We pride ourselves on be the best of the best. We mainly focus on cloud solutions and managed services. We need a business card that sets us apart from the other technology companies in the area and allows us to stand out.

Target Market(s)

Technology departments, CIO, CEOs, and Information Technology Staff.

Industry/Entity Type

Information Technology

Contact Information for Business Card

Must have the logo and our name.
Must have employee name, email address, office phone, cell phone and website.
Need to have all info on one side a cool design on backside.

Font styles to use
Serif
Sans Serif

Requirements
Must have
• Must have the logo and our name.
• Must have employee name, email address, office phone, cell phone and website.
• Need to have all info on one side a cool design on back side.
• Must be a crisp clean design, not too busy or confusing.

```html
<!DOCTYPE html>
<html lang="en">
<head>
<meta charset="utf-8">
<title>Vemtra Group – Business Card</title>
<link rel="stylesheet" href="https://fonts.googleapis.com/css2?family=Open+Sans:wght@400;600;700&family=Raleway:wght@400&display=swap">
<style>
  :root {
    --page-bg: #e9ebee;
    --card-bg: #ffffff;
    --ink: #333333;
    --ink-dark: #1e1e1e;
    --blue-deep: #1f6fc4;
    --blue-mid: #2a8fe0;
    --blue-bright: #27b4f5;
    --cyan-light: #7fd6fb;
    --tint: #eaf4fd;
    --white: #ffffff;
  }
  * { margin: 0; padding: 0; box-sizing: border-box; }
  html, body {
    width: 1105px; height: 1200px; overflow: hidden;
    background: var(--page-bg);
    font-family: "Open Sans", Arial, sans-serif;
  }
  .card {
    position: absolute;
    left: 196px;
    width: 720px; height: 412px;
    background: var(--card-bg);
    border-radius: 22px;
    overflow: hidden;
    box-shadow: 0 6px 18px rgba(0,0,0,0.18);
  }
  .card--front { top: 146px; }
  .card--back { top: 602px; }

  .card__wave { position: absolute; inset: 0; width: 100%; height: 100%; }

  .brand__mark {
    position: absolute; left: 104px; top: 34px;
    width: 112px; height: 112px; border-radius: 50%;
    background: var(--blue-bright);
  }
  .brand { position: absolute; left: 36px; top: 166px; }
  .brand__name {
    font-family: "Raleway", Arial, sans-serif;
    font-weight: 400; font-size: 40px; color: var(--ink);
    letter-spacing: 0.3px; line-height: 1;
  }
  .brand__url {
    margin-top: 9px; margin-left: 50px;
    font-weight: 700; font-size: 14px; color: var(--ink-dark);
  }

  .contact {
    position: absolute; right: 32px; top: 202px;
    text-align: right; color: var(--white);
  }
  .contact__name { font-weight: 700; font-size: 25px; line-height: 1.1; }
  .contact__role { font-size: 18px; line-height: 1.3; margin-bottom: 18px; }
  .contact__list { list-style: none; }
  .contact__item {
    display: flex; justify-content: flex-end; align-items: center; gap: 12px;
    font-size: 18px; line-height: 27.5px;
  }
  .contact__icon { width: 18px; height: 18px; fill: var(--white); flex: none; }

  .back-mark {
    position: absolute; left: 190px; top: 36px;
    width: 340px; height: 340px; border-radius: 50%;
    background: var(--tint);
  }
  .back-brand {
    position: absolute; left: 0; right: 0; top: 180px; text-align: center;
  }
  .back-brand__name {
    font-family: "Raleway", Arial, sans-serif;
    font-weight: 400; font-size: 58px; color: var(--ink);
    letter-spacing: 0.8px; line-height: 1;
  }
  .back-brand__url {
    margin-top: 12px; margin-left: 14px;
    font-weight: 700; font-size: 19px; color: var(--ink-dark);
  }
</style>
</head>
<body>

<section class="card card--front">
  <svg class="card__wave" viewBox="0 0 720 412" preserveAspectRatio="none" aria-hidden="true">
    <defs>
      <linearGradient id="band" x1="0" y1="1" x2="1" y2="0">
        <stop offset="0" stop-color="#1f6fc4"/>
        <stop offset="0.45" stop-color="#27b4f5"/>
        <stop offset="1" stop-color="#1f6fc4"/>
      </linearGradient>
    </defs>
    <path d="M0 330 C120 395 280 395 390 270 C480 160 580 78 720 70 L720 412 L0 412 Z" fill="url(#band)"/>
    <path d="M0 318 C130 380 290 372 392 262 C480 160 590 82 720 74" fill="none" stroke="#ffffff" stroke-width="4" opacity="0.9"/>
    <path d="M0 345 C130 410 300 410 410 300" fill="none" stroke="#ffffff" stroke-width="7"/>
    <path d="M0 360 C140 420 300 420 420 305" fill="none" stroke="#7fd6fb" stroke-width="12" opacity="0.85"/>
  </svg>

  <div class="brand__mark" aria-hidden="true"></div>
  <div class="brand">
    <div class="brand__name">Vemtra Group</div>
    <div class="brand__url">www.vemtragroup.com</div>
  </div>

  <div class="contact">
    <div class="contact__name">Daniel Marsh</div>
    <div class="contact__role">CEO/Founder</div>
    <ul class="contact__list">
      <li class="contact__item">614 202 7381
        <svg class="contact__icon" viewBox="0 0 24 24"><path d="M6.6 10.8c1.4 2.8 3.8 5.1 6.6 6.6l2.2-2.2c.3-.3.7-.4 1-.2 1.1.4 2.3.6 3.6.6.6 0 1 .4 1 1V20c0 .6-.4 1-1 1C10.6 21 3 13.4 3 4c0-.6.4-1 1-1h3.5c.6 0 1 .4 1 1 0 1.3.2 2.5.6 3.6.1.3 0 .7-.2 1l-2.3 2.2z"/></svg>
      </li>
      <li class="contact__item">614 559 0247
        <svg class="contact__icon" viewBox="0 0 24 24"><path d="M7 1h10a2 2 0 0 1 2 2v18a2 2 0 0 1-2 2H7a2 2 0 0 1-2-2V3a2 2 0 0 1 2-2zm0 3v14h10V4H7zm5 15.2a1.1 1.1 0 1 0 0 2.2 1.1 1.1 0 0 0 0-2.2z"/></svg>
      </li>
      <li class="contact__item">dmarsh@vemtra.com
        <svg class="contact__icon" viewBox="0 0 24 24"><path d="M2 5h20v14H2V5zm2 2v.4l8 5.2 8-5.2V7H4zm0 2.8V17h16V9.8l-8 5.2-8-5.2z"/></svg>
      </li>
      <li class="contact__item">www.vemtra.com
        <svg class="contact__icon" viewBox="0 0 24 24"><path d="M12 2a10 10 0 1 0 0 20 10 10 0 0 0 0-20zm-1 17.9A8 8 0 0 1 4.2 10.1L9 15v1a2 2 0 0 0 2 2v1.9zm6.9-2.5A2 2 0 0 0 16 16h-1v-3a1 1 0 0 0-1-1H8v-2h2a1 1 0 0 0 1-1V7h2a2 2 0 0 0 2-2v-.4a8 8 0 0 1 2.9 12.8z"/></svg>
      </li>
    </ul>
  </div>
</section>

<section class="card card--back">
  <div class="back-mark" aria-hidden="true"></div>
  <div class="back-brand">
    <div class="back-brand__name">Vemtra Group</div>
    <div class="back-brand__url">www.vemtragroup.com</div>
  </div>
</section>

</body>
</html>
```